card design for engineering consultancy

engineering drafting and project management company the provides drafting services for.
Electrical, Hydraulic, Mechanical, and Civil services
The company is called Q7R Services and logo is as attached
Information on card should be.
1. Logo
2.website : Q7RServices.example
3. email : info@Q7RServices.example
4. Phone: (+61) 400512836
5. Motto: Design - Document - Develop - Deliver

this card should be basically used for business identification only

Target Market(s)

electricians plumbers air conditioning installers and civil contractors

Industry/Entity Type

engineering, drafting, electrical, plumbing, airconditioning, civil

Contact Information for Business Card

1. Logo 2.website : Q7RServices.example 3. email : info@Q7RServices.example 4. Phone: (+61) 400512836 5. Motto: Design - Document - Develop - Deliver

Font styles to use
Serif

Requirements
Must have
• logo
Nice to have
• something inovative and different that makes it stand out from being just another business card

```html
<!DOCTYPE html>
<html lang="en">
<head>
<meta charset="utf-8">
<title>Q7R Services – Business Card</title>
<link rel="stylesheet" href="https://fonts.googleapis.com/css2?family=Noto+Serif:wght@400;700&display=swap">
<style>
  :root {
    --brand-red: #cf2027;
    --brand-charcoal: #545150;
    --ink: #2b2b2b;
    --paper: #ffffff;
    --page: #ffffff;
    --card-edge: #e2e2e2;
  }
  * { box-sizing: border-box; margin: 0; padding: 0; }
  html, body {
    width: 1200px; height: 896px; overflow: hidden;
    background: var(--page);
    font-family: "Noto Serif", Georgia, serif;
  }
  .canvas { position: relative; width: 1200px; height: 896px; }

  .card {
    position: absolute;
    left: 334px;
    width: 527px; height: 302px;
    background: var(--paper);
    border-radius: 26px;
    border: 1px solid var(--card-edge);
    overflow: hidden;
  }
  .card--front { top: 125px; }
  .card--back  { top: 471px; }

  /* Front */
  .wordmark {
    position: absolute;
    display: flex; align-items: center; gap: 8px;
    color: var(--brand-charcoal);
    font-weight: 700;
    white-space: nowrap;
  }
  .wordmark__square { background: var(--brand-red); flex: none; }
  .card--front .wordmark { left: 66px; top: 160px; font-size: 24px; }
  .card--front .wordmark__square { width: 14px; height: 14px; }

  .divider {
    position: absolute; left: 288px; top: 70px;
    width: 2px; height: 162px; background: var(--brand-red);
  }
  .holder { position: absolute; left: 299px; top: 64px; color: var(--ink); }
  .holder__name {
    color: var(--brand-red); font-weight: 700; font-size: 20px; line-height: 1.1;
  }
  .holder__role { font-size: 12.5px; margin-top: 3px; }
  .motto { font-size: 12.5px; line-height: 20px; margin-top: 18px; }
  .contact { list-style: none; margin-top: 10px; font-size: 12.5px; }
  .contact li { display: flex; align-items: center; gap: 7px; height: 20px; }
  .contact svg { width: 11px; height: 11px; fill: var(--brand-red); flex: none; }

  .footer-band {
    position: absolute; left: 0; right: 0; bottom: 0;
    height: 44px;
    background: linear-gradient(180deg, var(--brand-charcoal) 0%, var(--brand-red) 55%, var(--brand-red) 100%);
  }

  /* Back */
  .card--back .wordmark {
    left: 0; right: 0; top: 112px; justify-content: center;
    font-size: 58px; gap: 16px;
  }
  .card--back .wordmark__square { width: 34px; height: 34px; }
</style>
</head>
<body>
<main class="canvas">

  <section class="card card--front" aria-label="Business card front">
    <div class="wordmark"><span class="wordmark__square"></span>Q7R Services</div>

    <div class="divider"></div>

    <div class="holder">
      <h1 class="holder__name">ALAN BROOKS</h1>
      <p class="holder__role">Managing Director</p>
      <p class="motto">Motto: Design - Document<br>- Develop - Deliver</p>
      <ul class="contact">
        <li>
          <svg viewBox="0 0 24 24" aria-hidden="true"><path d="M6.6 10.8a15.1 15.1 0 0 0 6.6 6.6l2.2-2.2c.3-.3.7-.4 1-.2 1.1.4 2.3.6 3.6.6.6 0 1 .4 1 1V20c0 .6-.4 1-1 1C10.6 21 3 13.4 3 4c0-.6.4-1 1-1h3.5c.6 0 1 .4 1 1 0 1.3.2 2.5.6 3.6.1.3 0 .7-.2 1z"/></svg>
          (+61) 400512836
        </li>
        <li>
          <svg viewBox="0 0 24 24" aria-hidden="true"><path d="M2 5h20v2.2l-10 6-10-6z"/><path d="M2 9.5l10 6 10-6V19H2z"/></svg>
          info@Q7RServices.example
        </li>
        <li>
          <svg viewBox="0 0 24 24" aria-hidden="true"><path d="M12 2a10 10 0 1 0 0 20 10 10 0 0 0 0-20zm0 2.2c1.2 1.4 2 3.6 2.2 6.8H9.8c.2-3.2 1-5.4 2.2-6.8zM4.3 13h3.5c.1 2.3.6 4.4 1.4 6A8 8 0 0 1 4.3 13zm3.5-2H4.3a8 8 0 0 1 4.9-6c-.8 1.6-1.3 3.7-1.4 6zm4.2 8.8c-1.2-1.4-2-3.6-2.2-6.8h4.4c-.2 3.2-1 5.4-2.2 6.8zm2.8-.8c.8-1.6 1.3-3.7 1.4-6h3.5a8 8 0 0 1-4.9 6zm1.4-8c-.1-2.3-.6-4.4-1.4-6a8 8 0 0 1 4.9 6z"/></svg>
          Q7RServices.example
        </li>
      </ul>
    </div>

    <div class="footer-band" role="img" aria-label="Decorative red and charcoal wave band along the bottom edge"></div>
  </section>

  <section class="card card--back" aria-label="Business card back">
    <div class="wordmark"><span class="wordmark__square"></span>Q7R Services</div>
  </section>

</main>
</body>
</html>
```